Bathroom Remodeling Guide Needed

We need to create a Bathroom remodeling guide that we can give away as a freemium download. The attached file contains the instructions and copy for the guide along with our logo. Below is a dropbox link to our assets folder as well.

https://www.filevaultora.net/sh/fo/k7trw2mzq9plv804bxnhe/QJTmVzaPwErKs5yUxLcHoBn4?key=7hfpt2c9048rwq1ma5517j39m&dl=0

```html
<!DOCTYPE html>
<html lang="en">
<head>
<meta charset="utf-8">
<title>Bathroom Remodeling Guide – Crestline Kitchen &amp; Bath</title>
<link href="https://fonts.googleapis.com/css2?family=Poppins:wght@400;500;600;700;800&display=swap" rel="stylesheet">
<style>
:root{
  --backdrop:#7c7c7c;
  --paper:#ffffff;
  --brown:#76645a;
  --brown-dark:#5e4f46;
  --ink:#2f2f2f;
  --body:#4a4a4a;
  --mute:#c4c4c4;
  --accent:#e0651f;
  --line:#9a9a9a;
}
*{margin:0;padding:0;box-sizing:border-box}
html,body{width:1200px;height:3000px;overflow:hidden}
body{background:var(--backdrop);font-family:"Poppins",sans-serif;color:var(--body);position:relative}
.page{position:absolute;width:342px;height:443px;background:var(--paper);overflow:hidden;box-shadow:0 3px 10px rgba(0,0,0,.35)}
.abs{position:absolute}
.photo{position:absolute}
.tone-warm{background:linear-gradient(135deg,#8a6a52,#d8cdc2 55%,#a88a70)}
.tone-marble{background:linear-gradient(135deg,#cfcac5,#eeebe7 50%,#b8b0a8)}
.tone-grey{background:linear-gradient(135deg,#9c9893,#dcd8d3 60%,#8a857f)}
.tone-bright{background:linear-gradient(135deg,#e9e6e1,#fbfaf8 50%,#d9cfc3)}
.tone-navy{background:linear-gradient(135deg,#3f4a5e,#e8e8ea 45%,#cfd2d8 70%,#4a5468)}
.tone-site{background:linear-gradient(135deg,#8a5a3a,#c89a6a 45%,#6a4a3a)}
.tone-dark{background:linear-gradient(135deg,#d7d9db,#f3f3f3 50%,#3a3a3c)}
.tone-sunny{background:linear-gradient(135deg,#f2e6cf,#fbf6ea 50%,#d9472a)}
.tone-wood{background:linear-gradient(135deg,#9a6a3e,#c89462)}
.tone-sketch{background:linear-gradient(135deg,#ffffff,#eeeeee 60%,#d9b08a)}
.tone-portrait{background:linear-gradient(160deg,#8c8c8c,#c9a58a 55%,#5a5f6a)}

.brand{position:absolute;font-weight:600;color:var(--ink);letter-spacing:.03em;white-space:nowrap;line-height:1}
.brand.big{left:0;width:342px;text-align:center;font-size:15px}
.brand.small{font-size:7px}
.foot-brand{left:36px;top:391px}
.foot-url{position:absolute;right:33px;top:393px;font-size:5.4px;color:var(--ink);font-weight:500}
.foot-url b{color:var(--accent);font-weight:500}

.ghost{position:absolute;left:35px;font-weight:800;color:var(--mute);font-size:17px;line-height:1.05;letter-spacing:.01em;text-transform:uppercase}
.sub{position:absolute;left:35px;padding-left:8px;border-left:2.5px solid var(--brown);font-weight:800;color:var(--brown);font-size:12px;line-height:1.1;text-transform:uppercase}
.copy{position:absolute;font-size:5px;line-height:1.45;color:var(--body)}
.copy p{margin-bottom:5px}
.copy strong{color:var(--ink)}
.label{font-weight:700;color:var(--brown);font-size:7px;text-transform:uppercase;margin:6px 0 5px}
.ticks{display:grid;grid-template-columns:1fr 1fr;gap:4px 12px;list-style:none;margin-bottom:6px}
.ticks li{display:flex;gap:4px;align-items:flex-start}
.ticks svg{flex:none;width:6px;height:6px}
.vertical{position:absolute;writing-mode:vertical-rl;transform:rotate(180deg);font-weight:800;color:var(--mute);letter-spacing:.02em}
</style>
</head>
<body>
<svg width="0" height="0" style="position:absolute">
  <defs>
    <symbol id="tick" viewBox="0 0 10 10"><circle cx="5" cy="5" r="5" fill="#76645a"/><path d="M2.6 5.2l1.6 1.6 3.2-3.4" fill="none" stroke="#fff" stroke-width="1.3"/></symbol>
  </defs>
</svg>

<!-- Cover -->
<section class="page" style="left:197px;top:110px">
  <div class="brand big" style="top:29px">CRESTLINE</div>
  <div class="abs" style="left:41px;top:71px;width:260px;height:8px;border:1px solid var(--line);border-bottom:none"></div>
  <div class="photo tone-warm" style="left:0;top:86px;width:342px;height:175px" role="img" aria-label="Luxury bathroom with freestanding tub, marble walls and walk-in glass shower"></div>
  <div class="abs" style="left:41px;top:264px;width:260px;height:136px;border:1px solid var(--line);border-top:none"></div>
  <div class="abs" style="left:0;width:342px;top:272px;text-align:center;color:var(--ink)">
    <div style="font-size:10px">The Homeowner's Guide to</div>
    <div style="font-size:29px;font-weight:800;color:var(--brown);line-height:.92;margin-top:2px">BATHROOM<br>REMODELING</div>
    <div style="font-size:13px;letter-spacing:.06em;margin-top:1px">IN <b style="font-weight:800">CHARLOTTE</b></div>
    <div style="width:20px;height:3px;margin:7px auto 6px;background:repeating-linear-gradient(90deg,var(--brown) 0 3px,transparent 3px 5px)"></div>
    <div style="font-size:7.2px;line-height:1.3">How to Plan, Design, and Build a Bathroom<br>You'll Love for Years to Come</div>
  </div>
  <div class="abs" style="left:0;width:342px;top:413px;text-align:center;font-size:8px;letter-spacing:.28em;color:var(--ink)">www.<b>crestline</b><b style="color:var(--accent)">clt</b>.com</div>
</section>

<!-- Consultation -->
<section class="page" style="left:663px;top:110px">
  <div class="brand big" style="top:62px">CRESTLINE</div>
  <div class="abs" style="left:49px;top:106px;width:243px;height:204px;border:1px solid var(--line);border-bottom:none"></div>
  <div class="photo tone-bright" style="left:35px;top:132px;width:88px;height:87px" role="img" aria-label="Bright bathroom with vanity and tiled floor"></div>
  <div class="photo tone-wood" style="left:127px;top:132px;width:88px;height:87px" role="img" aria-label="Bathroom with wood vanity and window"></div>
  <div class="photo tone-grey" style="left:220px;top:132px;width:88px;height:87px" role="img" aria-label="Walk-in shower with dark tile and glass"></div>
  <div class="abs" style="left:0;width:342px;top:234px;text-align:center">
    <div style="font-size:11.5px;font-weight:800;color:var(--brown)">LET'S DESIGN YOUR BATHROOM</div>
    <div style="font-size:5.2px;margin-top:5px">The best place to start is with a conversation.</div>
    <div style="font-size:5.2px;margin-top:5px;line-height:1.35">We'll help you clarify your vision, explore your options, and create a plan tailored<br>specifically to your home.</div>
    <div style="display:inline-block;margin-top:7px;background:var(--brown);color:#fff;font-size:6.3px;font-weight:700;padding:3px 12px;border-radius:8px">SCHEDULE YOUR DESIGN CONSULTATION</div>
  </div>
  <div class="abs" style="left:0;top:316px;width:342px;height:127px;background:var(--brown)"></div>
  <div class="abs" style="left:45px;top:336px;color:#fff;font-size:8.6px;line-height:16px">
    <div style="display:flex;gap:6px;align-items:center"><svg width="10" height="10" viewBox="0 0 10 10"><circle cx="5" cy="5" r="5" fill="#fff"/><path d="M3.2 2.6l1 1-.5.7a3.5 3.5 0 0 0 2 2l.7-.5 1 1-.7.8c-1.8 0-4.3-2.5-4.3-4.3z" fill="#76645a"/></svg>+1 (704) 555-0148</div>
    <div style="display:flex;gap:6px;align-items:center"><svg width="10" height="10" viewBox="0 0 10 10"><circle cx="5" cy="5" r="5" fill="#fff"/><rect x="2.5" y="3.3" width="5" height="3.6" fill="none" stroke="#76645a" stroke-width=".8"/><path d="M2.5 3.3l2.5 2 2.5-2" fill="none" stroke="#76645a" stroke-width=".8"/></svg>info@CrestlineCLT.com</div>
    <div style="display:flex;gap:6px;align-items:center"><svg width="10" height="10" viewBox="0 0 10 10"><path d="M5 .5a3.3 3.3 0 0 1 3.3 3.3C8.3 6.3 5 9.5 5 9.5S1.7 6.3 1.7 3.8A3.3 3.3 0 0 1 5 .5z" fill="#fff"/><circle cx="5" cy="3.8" r="1.2" fill="#76645a"/></svg>Charlotte, NC</div>
    <div style="display:flex;gap:6px;align-items:center"><svg width="10" height="10" viewBox="0 0 10 10"><circle cx="5" cy="5" r="5" fill="#fff"/><circle cx="5" cy="5" r="2.8" fill="none" stroke="#76645a" stroke-width=".7"/><path d="M2.2 5h5.6M5 2.2v5.6" stroke="#76645a" stroke-width=".6"/></svg>www.crestline<span style="color:var(--accent)">clt</span>.com</div>
  </div>
  <div class="photo tone-portrait" style="left:177px;top:336px;width:70px;height:66px" role="img" aria-label="Portrait of the owner and general contractor"></div>
  <div class="abs" style="left:247px;top:336px;width:54px;height:66px;border:1px solid #cdbfb5;background:#8f7c71;color:#fff;font-size:7px;line-height:1.2;padding:17px 0 0 8px">Owner &amp;<br>General<br>Contractor</div>
</section>

<!-- Introduction -->
<section class="page" style="left:197px;top:581px">
  <div class="vertical" style="left:30px;top:42px;height:324px;font-size:38px">INTRODUCTION</div>
  <div class="sub" style="left:94px;top:42px;font-size:11.5px">BEFORE YOU START YOUR<br>BATHROOM REMODEL</div>
  <div class="copy" style="left:96px;top:78px;width:212px">
    <p>Remodeling your bathroom is one of the most impactful upgrades you can make to your home. Done right, it improves how you start and end your day, increases your home's value, and creates a space that feels both functional and refined.</p>
    <p>But without the right plan, it can quickly become overwhelming.</p>
    <p>Many homeowners begin with inspiration photos and good intentions, only to run into unexpected costs, delays, and decisions they weren't prepared for.</p>
    <p>This guide was created to give you clarity before you begin—so you can move forward with confidence, avoid common mistakes, and ultimately achieve a result you'll be proud of for years to come.</p>
  </div>
  <div class="photo tone-warm" style="left:96px;top:191px;width:212px;height:175px" role="img" aria-label="Modern bathroom with wood vanity and glass shower"></div>
  <div class="brand small foot-brand">CRESTLINE</div>
  <div class="foot-url">www.crestline<b>clt</b>.com &nbsp;| 01</div>
</section>

<!-- Biggest mistake -->
<section class="page" style="left:663px;top:581px">
  <div class="ghost" style="top:23px">THE BIGGEST MISTAKE<br>HOMEOWNERS MAKE</div>
  <div class="sub" style="top:67px">MOST BATHROOM REMODELS GO<br>WRONG BEFORE THEY EVEN START</div>
  <div class="copy" style="left:48px;top:100px;width:262px">
    <p>The success of a bathroom remodel is determined long before construction begins.</p>
    <p>The most common mistake homeowners make is starting without a clear, well-thought-out plan. Decisions are made on the fly, materials are selected too late, and small issues quickly turn into costly problems.</p>
    <div class="label">A SUCCESSFUL PROJECT REQUIRES</div>
    <ul class="ticks">
      <li><svg><use href="#tick"/></svg>A clear design vision</li>
      <li><svg><use href="#tick"/></svg>Proper planning before demolition</li>
      <li><svg><use href="#tick"/></svg>Thoughtful material selection</li>
      <li><svg><use href="#tick"/></svg>A team that understands both design and construction</li>
    </ul>
    <p>When these elements are in place, the process becomes smooth, predictable, and even enjoyable.</p>
    <p>When they're not, the experience is often the opposite.</p>
  </div>
  <div class="photo tone-grey" style="left:35px;top:226px;width:271px;height:146px" role="img" aria-label="Concrete-toned bathroom with round mirror, floating vanity and rain shower"></div>
  <div class="brand small foot-brand">CRESTLINE</div>
  <div class="foot-url">www.crestline<b>clt</b>.com &nbsp;| 02</div>
</section>

<!-- Investment -->
<section class="page" style="left:197px;top:1053px">
  <div class="abs" style="left:286px;top:0;width:56px;height:213px;background:var(--brown)"></div>
  <div class="ghost" style="left:38px;top:24px">WHAT SHOULD YOU<br>EXPECT TO INVEST?</div>
  <div class="photo tone-bright" style="left:0;top:69px;width:306px;height:144px" role="img" aria-label="Bright bathroom with freestanding tub and double wood vanity"></div>
  <div class="sub" style="left:38px;top:225px">UNDERSTANDING BATHROOM<br>REMODELING COSTS</div>
  <div class="copy" style="left:48px;top:258px;width:262px">
    <p>Every bathroom remodel is unique, but most projects fall within a predictable range depending on size, scope, and finishes.</p>
    <p>At Crestline Kitchen &amp; Bath, most bathroom remodeling projects <strong>start at $35,000 and increase based on complexity, materials, and customization.</strong></p>
    <div class="label">SEVERAL FACTORS INFLUENCE THE TOTAL INVESTMENT</div>
    <ul class="ticks">
      <li><svg><use href="#tick"/></svg>The size of the space</li>
      <li><svg><use href="#tick"/></svg>Custom vanities and cabinetry</li>
      <li><svg><use href="#tick"/></svg>Tile selection and layout complexity</li>
      <li><svg><use href="#tick"/></svg>Lighting and fixture upgrades</li>
      <li><svg><use href="#tick"/></svg>Plumbing or layout changes</li>
      <li><svg><use href="#tick"/></svg>Specialty features such as walk-in showers or freestanding tubs</li>
    </ul>
    <p>Rather than focusing on the lowest possible cost, our approach is to deliver long-term value—combining thoughtful design, quality materials, and expert craftsmanship.</p>
  </div>
  <div class="brand small foot-brand">CRESTLINE</div>
  <div class="foot-url">www.crestline<b>clt</b>.com &nbsp;| 03</div>
</section>

<!-- Design first -->
<section class="page" style="left:663px;top:1053px">
  <div class="ghost" style="top:33px">THE BIGGEST MISTAKE<br>HOMEOWNERS MAKE</div>
  <div class="sub" style="top:86px">MOST BATHROOM REMODELS GO<br>WRONG BEFORE THEY EVEN START</div>
  <div class="abs" style="left:0;top:153px;width:342px;height:189px;background:var(--brown)"></div>
  <div class="copy" style="left:36px;top:168px;width:102px;color:#fff;font-size:4.8px;line-height:1.3">
    <p>A beautiful bathroom doesn't happen by accident—it is designed.</p>
    <p>Layout, lighting, storage, and material selection must all work together to create a space that feels cohesive and functions effortlessly.</p>
    <p>Every project we take on includes a professional designer at no additional cost. This ensures that your bathroom is carefully planned before construction begins, eliminating guesswork and reducing the likelihood of costly changes later.</p>
    <p>With a clear design in place, you'll be able to visualize your new space, make confident decisions, and move into construction with clarity.</p>
  </div>
  <div class="photo tone-sketch" style="left:142px;top:132px;width:175px;height:233px;border:1px solid #8a8a8a" role="img" aria-label="Hands framing a line sketch of a bathroom design plan"></div>
  <div class="brand small foot-brand">CRESTLINE</div>
  <div class="foot-url">www.crestline<b>clt</b>.com &nbsp;| 04</div>
</section>

<!-- Process -->
<section class="page" style="left:197px;top:1524px">
  <div class="photo tone-site" style="left:36px;top:17px;width:306px;height:148px" role="img" aria-label="Bathroom under construction with exposed framing and plumbing"></div>
  <div class="ghost" style="left:36px;top:177px;font-size:16px">THE REMODELING PROCESS</div>
  <div class="sub" style="left:36px;top:198px">WHAT TO EXPECT WHEN YOU<br>WORK WITH US</div>
  <div class="copy" style="left:48px;top:232px;width:262px">
    <p>A structured process is what separates a stressful remodel from a smooth one.</p>
    <p>Here's how we guide you through each phase:</p>
  </div>
  <div class="abs" style="left:226px;top:262px;width:82px;height:108px;border:1px solid var(--line);border-left:none"></div>
  <div class="copy" style="left:46px;top:264px;width:262px;display:grid;grid-template-columns:135px 120px;gap:7px 0;font-size:4.6px;line-height:1.3">
    <div style="display:flex;gap:4px"><svg width="11" height="11" style="flex:none"><circle cx="5.5" cy="5.5" r="5.5" fill="#76645a"/></svg><div><div class="label" style="margin:0 0 2px;font-size:6px">CONSULTATION &amp; VISION</div>We begin by understanding your goals, your style, and how you want your space to function.</div></div>
    <div style="display:flex;gap:4px"><svg width="11" height="11" style="flex:none"><rect width="11" height="11" rx="2" fill="#76645a"/></svg><div><div class="label" style="margin:0 0 2px;font-size:6px">CONSTRUCTION</div>Our team executes the project with attention to detail, cleanliness, and respect for your home.</div></div>
    <div style="display:flex;gap:4px"><svg width="11" height="11" style="flex:none"><circle cx="5.5" cy="5.5" r="5.5" fill="#76645a"/></svg><div><div class="label" style="margin:0 0 2px;font-size:6px">MEASUREMENT &amp; DESIGN</div>We take precise measurements and develop a professional design plan tailored to your space.</div></div>
    <div style="display:flex;gap:4px"><svg width="11" height="11" style="flex:none"><circle cx="5.5" cy="5.5" r="5.5" fill="#76645a"/></svg><div><div class="label" style="margin:0 0 2px;font-size:6px">FINAL WALKTHROUGH</div>We review every detail together to ensure everything meets our standards—and yours.</div></div>
    <div style="display:flex;gap:4px"><svg width="11" height="11" style="flex:none"><circle cx="5.5" cy="5.5" r="5.5" fill="#76645a"/></svg><div><div class="label" style="margin:0 0 2px;font-size:6px">MATERIAL SELECTION</div>We guide you through selecting materials, finishes, and fixtures that align with your vision and investment level.</div></div>
  </div>
  <div class="brand small foot-brand">CRESTLINE</div>
  <div class="foot-url">www.crestline<b>clt</b>.com &nbsp;| 05</div>
</section>

<!-- Timeline -->
<section class="page" style="left:663px;top:1524px">
  <div class="ghost" style="top:31px">TIMELINE EXPECTATIONS</div>
  <div class="sub" style="top:58px">HOW LONG DOES A BATHROOM<br>REMODEL TAKE?</div>
  <div class="copy" style="left:48px;top:92px;width:262px">
    <p>One of the most common questions we hear is: "How long will this take?"</p>
    <p>While every project is different, most bathroom remodels take:</p>
    <ul class="ticks" style="grid-template-columns:1fr">
      <li><svg><use href="#tick"/></svg>3–5 weeks during construction</li>
      <li><svg><use href="#tick"/></svg>6–10 weeks total including planning<br>and design</li>
    </ul>
    <p>The planning phase is critical. When decisions are made upfront, construction moves efficiently and delays are minimized.</p>
  </div>
  <div class="photo tone-navy" style="left:35px;top:196px;width:307px;height:170px" role="img" aria-label="Large bathroom with navy cabinetry, freestanding tub and chandelier"></div>
  <div class="brand small foot-brand">CRESTLINE</div>
  <div class="foot-url">www.crestline<b>clt</b>.com &nbsp;| 06</div>
</section>

<!-- Features -->
<section class="page" style="left:197px;top:1995px">
  <div class="abs" style="left:0;top:0;width:40px;height:180px;background:var(--brown)"></div>
  <div class="photo tone-dark" style="left:40px;top:0;width:302px;height:180px" role="img" aria-label="Modern bathroom with black freestanding tub and glass shower"></div>
  <div class="ghost" style="left:36px;top:194px">FEATURES THAT ADD THE<br>MOST VALUE</div>
  <div class="sub" style="left:36px;top:240px">POPULAR UPGRADES<br>HOMEOWNERS LOVE</div>
  <div class="copy" style="left:48px;top:275px;width:262px">
    <p>Today's bathrooms are designed to feel like personal retreats. Some of the most requested features include:</p>
    <ul class="ticks">
      <li><svg><use href="#tick"/></svg>Walk-in showers with frameless glass</li>
      <li><svg><use href="#tick"/></svg>Freestanding soaking tubs</li>
      <li><svg><use href="#tick"/></svg>Floating or custom vanities</li>
      <li><svg><use href="#tick"/></svg>LED backlit mirrors</li>
      <li><svg><use href="#tick"/></svg>Heated tile flooring</li>
      <li><svg><use href="#tick"/></svg>Custom storage solutions</li>
    </ul>
    <p>These features not only improve daily comfort but also add long-term value to your home.</p>
  </div>
  <div class="brand small foot-brand">CRESTLINE</div>
  <div class="foot-url">www.crestline<b>clt</b>.com &nbsp;| 07</div>
</section>

<!-- Before & after -->
<section class="page" style="left:663px;top:1995px">
  <div class="ghost" style="top:51px">BEFORE &amp; AFTER<br>TRANSFORMATION</div>
  <div class="sub" style="top:103px;font-size:11.5px">FROM OUTDATED TO EXCEPTIONAL</div>
  <div class="copy" style="left:48px;top:124px;width:262px">
    <p>One of the most rewarding parts of what we do is transforming a space that no longer works into one that feels entirely new.</p>
    <p>Below is an example of a small bathroom renovation where we improved functionality, updated materials, and created a clean, modern design.</p>
    <ul class="ticks">
      <li><svg><use href="#tick"/></svg>Walk-in showers with frameless glass</li>
      <li><svg><use href="#tick"/></svg>Freestanding soaking tubs</li>
      <li><svg><use href="#tick"/></svg>Floating or custom vanities</li>
      <li><svg><use href="#tick"/></svg>LED backlit mirrors</li>
      <li><svg><use href="#tick"/></svg>Heated tile flooring</li>
      <li><svg><use href="#tick"/></svg>Custom storage solutions</li>
    </ul>
    <p>These features not only improve daily comfort but also add long-term value to your home.</p>
  </div>
  <div class="photo tone-wood" style="left:35px;top:248px;width:87px;height:84px" role="img" aria-label="Bathroom before renovation"></div>
  <div class="photo tone-wood" style="left:129px;top:248px;width:87px;height:84px" role="img" aria-label="Bathroom during construction"></div>
  <div class="photo tone-grey" style="left:222px;top:248px;width:85px;height:84px" role="img" aria-label="Bathroom after renovation"></div>
  <div class="abs" style="left:41px;top:337px;width:75px;height:11px;background:var(--brown);color:#fff;font-size:5.5px;font-weight:600;text-align:center;line-height:11px">Before</div>
  <div class="abs" style="left:135px;top:337px;width:75px;height:11px;background:var(--brown);color:#fff;font-size:5.5px;font-weight:600;text-align:center;line-height:11px">During construction</div>
  <div class="abs" style="left:227px;top:337px;width:75px;height:11px;background:var(--brown);color:#fff;font-size:5.5px;font-weight:600;text-align:center;line-height:11px">After</div>
  <div class="brand small foot-brand">CRESTLINE</div>
  <div class="foot-url">www.crestline<b>clt</b>.com &nbsp;| 08</div>
</section>

<!-- Contractor -->
<section class="page" style="left:197px;top:2464px">
  <div class="ghost" style="left:36px;top:37px">WHAT TO LOOK FOR IN<br>A CONTRACTOR</div>
  <div class="photo tone-bright" style="left:36px;top:88px;width:133px;height:134px" role="img" aria-label="Arched bathroom nook with freestanding tub"></div>
  <div class="photo tone-marble" style="left:176px;top:88px;width:132px;height:134px" role="img" aria-label="Bathroom with rounded mirror and floating vanity"></div>
  <div class="sub" style="left:36px;top:231px">CHOOSING THE RIGHT<br>REMODELING PARTNER</div>
  <div class="copy" style="left:48px;top:264px;width:262px">
    <p>The contractor you choose will ultimately determine your experience and your outcome.</p>
    <p>When evaluating a remodeling company, look for:</p>
    <ul class="ticks">
      <li><svg><use href="#tick"/></svg>A clear and defined process</li>
      <li><svg><use href="#tick"/></svg>Transparent and realistic pricing</li>
      <li><svg><use href="#tick"/></svg>Strong communication from start to finish</li>
      <li><svg><use href="#tick"/></svg>A portfolio of completed projects</li>
      <li><svg><use href="#tick"/></svg>Design capabilities—not just construction</li>
      <li><svg><use href="#tick"/></svg>Positive client experiences and reviews</li>
    </ul>
    <p>The right partner will make the process feel organized, predictable, and well-managed.</p>
  </div>
  <div class="brand small foot-brand">CRESTLINE</div>
  <div class="foot-url">www.crestline<b>clt</b>.com &nbsp;| 09</div>
</section>

<!-- Testimonials -->
<section class="page" style="left:663px;top:2464px">
  <div class="vertical" style="left:30px;top:30px;height:350px;font-size:27px;text-align:center">WHAT OUR CLIENTS SAY</div>
  <div class="photo tone-sunny" style="left:93px;top:0;width:249px;height:181px" role="img" aria-label="Small bathroom with round mirror, wood vanity and red tile"></div>
  <div class="sub" style="left:93px;top:197px;font-size:11.5px">CLIENT EXPERIENCES</div>
  <div class="copy" style="left:93px;top:222px;width:216px;font-size:4.7px;line-height:1.35">
    <div style="font-size:14px;color:var(--mute);font-weight:700;line-height:.8">“</div>
    <p>Crestline Kitchen and Bath just completed a two full bath and one powder room renovation for me. I cannot say enough good things about the team. We were kept informed throughout the process and checked on progress of the project throughout. The team and subcontractors all performed very well. They cleaned up after themselves every day and took extra care of my home. I highly recommend Crestline Kitchen and Bath.</p>
    <p style="text-align:right;font-weight:600;color:var(--ink);font-size:5.5px"><b>Dana Whitfield,</b> Charlotte NC</p>
    <div style="font-size:14px;color:var(--mute);font-weight:700;line-height:.8;margin-top:6px">“</div>
    <p>I can't say enough about my experience with the team at Crestline Kitchen &amp; Bath. Far different and BETTER than any other experience we have had with other contractors. They were transparent with pricing, stayed within budget, and even finished ahead of schedule.</p>
    <p style="text-align:right;font-weight:600;color:var(--ink);font-size:5.5px"><b>Marisol,</b> Charlotte NC</p>
  </div>
  <div class="brand small foot-brand">CRESTLINE</div>
  <div class="foot-url">www.crestline<b>clt</b>.com &nbsp;| 10</div>
</section>
</body>
</html>
```